4"x9" Roofing Flyer Design - Tile Roofing!

We are looking to create a 4"x9" double sided flyer in full color that displays pictures of before and after of tile underlayment replacement. This would have words as well.

The theme should match the overall theme of our brochure that we already have designed so they are cohesive.

I have uploaded an example of a similar flyer that we like the overall layout of.

Please read the "Design Wording" PDF I uploaded for the words and overall design layout we are looking for on this brochure.

Please let me know if you'd like more photos or anything like that.

Target Market(s)

Retirees

Industry/Entity Type

Roofing

Font styles to use
Other font styles liked:
• Match existing fonts from our brochure

Requirements
Must have
• Must match style of existing brochure (uploaded), font must match closely as well

```html
<!DOCTYPE html>
<html lang="en">
<head>
<meta charset="UTF-8">
<title>Mesa Ridge Roofing – Tile Underlayment Flyer</title>
<link rel="stylesheet" href="https://fonts.googleapis.com/css2?family=Arvo:wght@700&family=Cormorant+Garamond:wght@500;700&display=swap">
<style>
  :root {
    --orange: #e05a1e;
    --panel: #2c2c2c;
    --ground: #141414;
    --rule: #dcdcdc;
    --frame: #e7e3de;
    --ink: #ece6dc;
    --white: #ffffff;
  }
  * { margin: 0; padding: 0; box-sizing: border-box; }
  html, body { width: 1200px; height: 2700px; overflow: hidden; background: var(--ground); }
  .flyer {
    position: relative;
    width: 1200px;
    height: 2700px;
    background: var(--ground);
    overflow: hidden;
  }
  .header-shape { position: absolute; top: 0; left: 0; width: 1200px; height: 780px; }
  .brand {
    position: absolute;
    top: 200px;
    left: 0;
    width: 1200px;
    text-align: center;
    font-family: "Arvo", serif;
    font-weight: 700;
    font-size: 60px;
    color: var(--white);
  }
  .brand-mark {
    display: inline-block;
    width: 34px;
    height: 34px;
    background: var(--orange);
    margin-right: 18px;
    vertical-align: 4px;
  }
  .call {
    position: absolute;
    top: 346px;
    left: 0;
    width: 1200px;
    text-align: center;
    font-family: "Arvo", serif;
    font-weight: 700;
  }
  .call-label { font-size: 34px; color: var(--white); line-height: 1.3; }
  .call-number { font-size: 46px; color: var(--orange); line-height: 1.2; }

  .gallery {
    position: absolute;
    top: 822px;
    left: 100px;
    width: 990px;
    display: grid;
    grid-template-columns: 470px 470px;
    grid-template-rows: 470px 470px;
    column-gap: 50px;
    row-gap: 64px;
  }
  .photo-frame { background: var(--frame); padding: 12px; }
  .photo { width: 100%; height: 100%; }
  .photo--underlayment { background: linear-gradient(160deg, #8fa3b8 0%, #c9ccd0 30%, #a9adb1 70%, #7d7f80 100%); }
  .photo--tiles { background: linear-gradient(150deg, #c8b08e 0%, #9c8468 50%, #6d5a45 100%); }
  .photo--cracked { background: linear-gradient(170deg, #b9b6b0 0%, #8c8a86 50%, #4b4845 100%); }
  .photo--rot { background: linear-gradient(170deg, #4e4338 0%, #8a7863 50%, #5c4f41 100%); }

  .copy {
    position: absolute;
    top: 1876px;
    left: 106px;
    width: 988px;
    font-family: "Cormorant Garamond", serif;
    font-weight: 500;
    font-size: 34px;
    line-height: 42px;
    color: var(--ink);
    text-align: justify;
  }
  .copy-title {
    font-family: "Arvo", serif;
    font-weight: 700;
    font-size: 33px;
    line-height: 44px;
    color: var(--orange);
    text-align: left;
  }
  .copy p { margin-bottom: 16px; }
  .copy-lead { color: var(--orange); margin-top: 28px; margin-bottom: 4px !important; text-align: left; }
  .copy strong { font-weight: 700; color: var(--white); }
  .copy .tight { margin-bottom: 0; }

  .footer-shape { position: absolute; left: 0; bottom: 0; width: 1200px; height: 90px; }
</style>
</head>
<body>
<main class="flyer">
  <svg class="header-shape" viewBox="0 0 1200 780" aria-hidden="true">
    <polygon points="0,0 1200,0 1200,470 690,700 0,390" fill="var(--panel)"/>
    <polyline points="0,392 690,702 1200,472" fill="none" stroke="var(--rule)" stroke-width="10"/>
    <polygon points="0,404 690,714 1200,484 1200,522 690,754 0,442" fill="var(--orange)"/>
  </svg>

  <div class="brand"><span class="brand-mark"></span>Mesa Ridge Roofing</div>
  <div class="call">
    <div class="call-label">Call Now</div>
    <div class="call-number">(555) 214-7730</div>
  </div>

  <section class="gallery">
    <div class="photo-frame"><div class="photo photo--underlayment" role="img" aria-label="Roof deck with new synthetic underlayment and battens installed"></div></div>
    <div class="photo-frame"><div class="photo photo--tiles" role="img" aria-label="Finished tan tile roof with vents"></div></div>
    <div class="photo-frame"><div class="photo photo--cracked" role="img" aria-label="Close-up of cracked, brittle old underlayment beneath tiles"></div></div>
    <div class="photo-frame"><div class="photo photo--rot" role="img" aria-label="Deteriorated underlayment and debris on the roof deck"></div></div>
  </section>

  <section class="copy">
    <h2 class="copy-title">The Hidden Clock Ticking Under Your Tiles</h2>
    <p>When a tile roof is installed, the tiles themselves are not waterproof - they are simply a shield. The actual waterproofing is done by the felt or synthetic underlayment installed beneath them.</p>
    <p class="copy-lead">In homes of your vintage, this underlayment is now:</p>
    <p><strong>Brittle and Chalky:</strong> It cracks and turns into powder under the constant heat cycles, losing its waterproofing integrity.</p>
    <p class="tight"><strong>Compromised:</strong> Even a single leak in a neighboring home means the moisture risk has increased exponentially across the entire block.</p>
    <p>Based on the age and materials used in this specific neighborhood, underlayment failure is not a matter of if, but when.</p>
    <p>Waiting for a visible ceiling stain often means the damage has already spread to the roof deck, rafters, and interior walls. A slow leak can silently cost thousands in remediation before you ever see a drop.</p>
  </section>

  <svg class="footer-shape" viewBox="0 0 1200 90" aria-hidden="true">
    <polyline points="800,100 960,40 1120,100" fill="none" stroke="var(--orange)" stroke-width="34"/>
  </svg>
</main>
</body>
</html>
```